Tallow Microsystems PowerPoint Master Slide Deck Design

This is a 2-phase project to design a slide deck for a semiconductor company in the Silicon Valley. The design budget will be increased with each phase.
The slide deck will need to have one version with a dark background for presentations and a second version with a white background. Otherwise, the slides will be the same. I anticipate we will need a total of 10 slides, but that number may change.
The first phase will be to design a Title and a Title and Content slide.
- The Title Slide is the first slide of the deck. It should include the presentation title, the presenter's name and date of presentation
- The Title and Content slide should include a title and content with bullet points and up to 2 additional sub-bullets
- The Title and Content slide should have a footer that includes the slide #, Tallow Microsystems Confidential, and the logo. This footer will be on every slide except the Title Slide
The first two slides will serve as the format for the remaining ~8 slides:
-Header and Content Text (1, 2, 4 column)
-Header and Content Image (bar chart, pie chart, tables)
-Break
-Title only
-Closing (Tallow logo only)
Our slides contain a lot of content so a clean and simple design is best.
Both phases will need to include pre-set color options for
-Text and Lines
-Shadows
-Bullets and sub-bullets (including shapes, ex. circle, slash, square, etc.)
-Bar charts, pie charts, tables
Samples of our collateral are attached. Logo files are also attached
Look and feel
Each slider illustrates characteristics of the customer's brand and the style your logo design should communicate.

```html
<!DOCTYPE html>
<html lang="en">
<head>
<meta charset="utf-8">
<title>Tallow Microsystems – Master Slide Deck</title>
<link rel="stylesheet" href="https://fonts.googleapis.com/css2?family=Montserrat:wght@400;500;600;700;800&display=swap">
<style>
:root{
  --page:#000000;
  --slide:#1f1f20;
  --ink:#ffffff;
  --soft:#d9dde0;
  --accent:#5ec4e8;
  --deep-blue:#0b2dff;
  --bright-blue:#1a86ff;
  --rule:#3d6f86;
  --footer-rule:#6b6b6b;
  --grid:#444444;
}
*{box-sizing:border-box;margin:0;padding:0}
html,body{width:875px;height:1200px;overflow:hidden;background:var(--page)}
body{position:relative;font-family:"Montserrat",sans-serif;color:var(--ink)}

.slide{position:absolute;width:386px;height:217px;background:var(--slide);overflow:hidden}
.slide > *{position:absolute}
.topbar{left:0;top:0;width:100%;height:3px;background:linear-gradient(90deg,var(--deep-blue),#14d2ff)}
.topbar.reverse{background:linear-gradient(90deg,#14d2ff,var(--deep-blue))}

.title{font-weight:700;font-size:19px;letter-spacing:1.3px;white-space:nowrap;line-height:1}
.hl{color:var(--accent)}
.title-rule{width:36px;height:1px;background:var(--ink)}

.footer-rule{left:30px;top:192px;width:326px;height:1px;background:var(--footer-rule)}
.footer-mark{left:54px;top:200px;font-size:6px;font-weight:600;letter-spacing:.3px;display:flex;align-items:center;gap:2px;line-height:1}
.footer-mark i{display:block;width:4px;height:4px;border:1px solid var(--ink);border-radius:50%}
.copyright{left:127px;top:201px;font-size:5.2px;letter-spacing:.9px;line-height:1;color:var(--soft)}
.slide-num{left:315px;top:201px;font-size:5px;font-weight:700;letter-spacing:.6px;line-height:1}

.num{font-weight:700;color:var(--accent);line-height:1}
.para{color:var(--soft);line-height:1.2}
.sub{color:var(--soft);line-height:1.2;padding-left:var(--indent,14px)}
.sub::before{content:"";position:absolute;left:0;top:var(--mid,4px);width:var(--dash,7px);height:1px;background:var(--accent)}
.sub::after{content:"";position:absolute;left:calc(var(--dash,7px) - 1px);top:calc(var(--mid,4px) - var(--dot,3px)/2 + .5px);width:var(--dot,3px);height:var(--dot,3px);border:1px solid var(--accent);border-radius:50%}

/* title slide */
.cover-rule{left:70px;top:47px;width:1.5px;height:124px;background:var(--ink)}
.cover-mark{left:90px;top:56px;display:flex;align-items:center;gap:5px;font-size:9px;font-weight:600;letter-spacing:.6px;line-height:1.1}
.cover-mark i{display:block;width:10px;height:10px;border:1.5px solid var(--ink);border-radius:50%}
.cover-title{left:86px;top:93px;font-size:23.5px;font-weight:700;line-height:1.18;letter-spacing:.2px}
.cover-meta{top:163px;font-size:7.4px;font-weight:600;letter-spacing:1.8px;line-height:1}
.cover-divider{left:204px;top:158px;width:1px;height:15px;background:var(--ink)}

/* content boxes */
.box{width:167px;height:48px;border:1px solid var(--rule)}
.box .num{position:absolute;left:8px;top:13px;font-size:23px}
.box h3{position:absolute;left:49px;top:7px;font-size:7px;font-weight:700;color:var(--accent);letter-spacing:.2px;line-height:1}
.box .para{position:absolute;left:49px;top:17px;width:112px;font-size:3.4px}
.box .sub{position:absolute;left:53px;font-size:3.4px;--dash:4px;--dot:2px;--mid:1.6px;--indent:8px;width:110px}

/* four columns */
.col-num{font-size:21px;top:69px}
.col-icon{top:70px}
.col-sub{top:95px;font-size:6.5px;font-weight:700;color:var(--accent);line-height:1;letter-spacing:.2px}
.col-para{top:116px;width:76px;font-size:5px}
.col-bullet{width:70px;font-size:3.6px;--dash:5px;--dot:2px;--mid:2px;--indent:15px}
.col-divider{top:81px;width:1px;height:86px;background:var(--rule)}
</style>
</head>
<body>

<!-- 1 · Title slide -->
<section class="slide" style="left:47px;top:38px">
  <div class="cover-rule"></div>
  <div class="cover-mark"><i></i><span>TALLOW<br>MICROSYSTEMS</span></div>
  <h1 class="cover-title">BUSINESS<br><span class="hl">PRESENTATION</span></h1>
  <p class="cover-meta" style="left:85px">PRESENTER’S NAME</p>
  <div class="cover-divider"></div>
  <p class="cover-meta" style="left:220px;letter-spacing:1.1px">DATE: 12-20-2024</p>
</section>

<!-- 2 · Four content boxes -->
<section class="slide" style="left:443px;top:38px">
  <div class="topbar"></div>
  <div class="title-rule" style="left:66px;top:10px"></div>
  <h2 class="title" style="left:66px;top:31px">YOUR <span class="hl">CONTENT</span> SLIDE</h2>

  <article class="box" style="left:23px;top:68px">
    <span class="num">01</span><h3>CONTENT HEADER</h3>
    <p class="para">Lorem ipsum dolor sit amet, consectetuer adipiscing elit. Aenean commodo ligula eget dolor. Aenean massa.</p>
    <p class="sub" style="top:30px">Lorem ipsum dolor sit amet, consectetuer adipiscing elit.</p>
    <p class="sub" style="top:38px">Lorem ipsum dolor sit amet, consectetuer adipiscing elit.</p>
  </article>
  <article class="box" style="left:196px;top:68px">
    <span class="num">02</span><h3>CONTENT HEADER</h3>
    <p class="para">Lorem ipsum dolor sit amet, consectetuer adipiscing elit. Aenean commodo ligula eget dolor. Aenean massa.</p>
    <p class="sub" style="top:30px">Lorem ipsum dolor sit amet, consectetuer adipiscing elit.</p>
    <p class="sub" style="top:38px">Lorem ipsum dolor sit amet, consectetuer adipiscing elit.</p>
  </article>
  <article class="box" style="left:23px;top:122px">
    <span class="num">03</span><h3>CONTENT HEADER</h3>
    <p class="para">Lorem ipsum dolor sit amet, consectetuer adipiscing elit. Aenean commodo ligula eget dolor. Aenean massa.</p>
    <p class="sub" style="top:30px">Lorem ipsum dolor sit amet, consectetuer adipiscing elit.</p>
    <p class="sub" style="top:38px">Lorem ipsum dolor sit amet, consectetuer adipiscing elit.</p>
  </article>
  <article class="box" style="left:196px;top:122px">
    <span class="num">04</span><h3>CONTENT HEADER</h3>
    <p class="para">Lorem ipsum dolor sit amet, consectetuer adipiscing elit. Aenean commodo ligula eget dolor. Aenean massa.</p>
    <p class="sub" style="top:30px">Lorem ipsum dolor sit amet, consectetuer adipiscing elit.</p>
    <p class="sub" style="top:38px">Lorem ipsum dolor sit amet, consectetuer adipiscing elit.</p>
  </article>

  <div class="footer-rule"></div>
  <div class="footer-mark"><i></i>TALLOW</div>
  <p class="copyright">©Copyright 2023 Tallow Microsystems.</p>
  <p class="slide-num">SLIDE #</p>
</section>

<!-- 3 · One column, two items -->
<section class="slide" style="left:47px;top:265px">
  <div class="topbar"></div>
  <div class="title-rule" style="left:51px;top:25px"></div>
  <h2 class="title" style="left:51px;top:31px">CONTENT <span class="hl">HEADER</span> SLIDE</h2>

  <span class="num" style="left:39px;top:82px;font-size:21px">01</span>
  <p class="para" style="left:87px;top:65px;width:245px;font-size:7px">Lorem ipsum dolor sit amet, consectetuer adipiscing elit. Aenean commodo ligula eget dolor. Aenean massa.</p>
  <p class="sub" style="left:113px;top:95px;font-size:6.6px">Lorem ipsum dolor sit amet, consectetuer adipiscing elit.</p>
  <p class="sub" style="left:113px;top:108px;font-size:6.6px">Lorem ipsum dolor sit amet, consectetuer adipiscing elit.</p>
  <div style="left:34px;top:124px;width:323px;height:1px;background:var(--rule)"></div>
  <span class="num" style="left:39px;top:148px;font-size:21px">02</span>
  <p class="para" style="left:87px;top:132px;width:245px;font-size:7px">Lorem ipsum dolor sit amet, consectetuer adipiscing elit. Aenean commodo ligula eget dolor. Aenean massa.</p>
  <p class="sub" style="left:113px;top:160px;font-size:6.6px">Lorem ipsum dolor sit amet, consectetuer adipiscing elit.</p>
  <p class="sub" style="left:113px;top:173px;font-size:6.6px">Lorem ipsum dolor sit amet, consectetuer adipiscing elit.</p>

  <div class="footer-rule"></div>
  <div class="footer-mark"><i></i>TALLOW</div>
  <p class="copyright">©Copyright 2023 Tallow Microsystems.</p>
  <p class="slide-num">SLIDE #</p>
</section>

<!-- 4 · Two columns -->
<section class="slide" style="left:443px;top:265px">
  <div class="topbar"></div>
  <div class="title-rule" style="left:50px;top:25px"></div>
  <h2 class="title" style="left:50px;top:31px">CONTENT <span class="hl">HEADER</span> SLIDE</h2>

  <span class="num" style="left:31px;top:78px;font-size:21px">01</span>
  <p class="para" style="left:67px;top:76px;width:115px;font-size:7px">Lorem ipsum dolor sit amet, consectetuer adipiscing elit. Aenean commodo ligula eget dolor. Aenean massa.</p>
  <p class="sub" style="left:66px;top:124px;width:120px;font-size:6.4px;--indent:17px;--dash:10px;--mid:4px">Lorem ipsum dolor sit amet, consectetuer adipiscing elit.</p>
  <p class="sub" style="left:66px;top:149px;width:120px;font-size:6.4px;--indent:17px;--dash:10px;--mid:4px">Lorem ipsum dolor sit amet, consectetuer adipiscing elit.</p>
  <div style="left:195px;top:77px;width:1px;height:102px;background:var(--rule)"></div>
  <span class="num" style="left:207px;top:78px;font-size:21px">02</span>
  <p class="para" style="left:242px;top:76px;width:115px;font-size:7px">Lorem ipsum dolor sit amet, consectetuer adipiscing elit. Aenean commodo ligula eget dolor. Aenean massa.</p>
  <p class="sub" style="left:242px;top:124px;width:120px;font-size:6.4px;--indent:17px;--dash:10px;--mid:4px">Lorem ipsum dolor sit amet, consectetuer adipiscing elit.</p>
  <p class="sub" style="left:242px;top:149px;width:120px;font-size:6.4px;--indent:17px;--dash:10px;--mid:4px">Lorem ipsum dolor sit amet, consectetuer adipiscing elit.</p>

  <div class="footer-rule"></div>
  <div class="footer-mark"><i></i>TALLOW</div>
  <p class="copyright">©Copyright 2023 Tallow Microsystems.</p>
  <p class="slide-num">SLIDE #</p>
</section>

<!-- 5 · Four columns -->
<section class="slide" style="left:47px;top:492px">
  <div class="topbar"></div>
  <div class="title-rule" style="left:51px;top:24px"></div>
  <h2 class="title" style="left:51px;top:30px">CONTENT <span class="hl">HEADER</span> SLIDE</h2>

  <span class="num col-num" style="left:30px">01</span>
  <svg class="col-icon" style="left:63px" width="28" height="14" viewBox="0 0 28 14" fill="none" stroke="#fff" stroke-width=".8">
    <circle cx="7" cy="4" r="2.3"/><circle cx="14" cy="4" r="2.3"/><circle cx="21" cy="4" r="2.3"/>
    <path d="M3 12c0-3 2-4.5 4-4.5s4 1.5 4 4.5M10 12c0-3 2-4.5 4-4.5s4 1.5 4 4.5M17 12c0-3 2-4.5 4-4.5s4 1.5 4 4.5"/>
  </svg>
  <p class="col-sub" style="left:26px">Subsection Title</p>
  <p class="para col-para" style="left:26px">Lorem ipsum dolor sit amet, consectetuer adipiscing elit. Aenean commodo ligula eget dolor. Aenean massa.</p>
  <p class="sub col-bullet" style="left:30px;top:147px">Lorem ipsum dolor sit amet, consectetuer adipiscing elit.</p>
  <p class="sub col-bullet" style="left:30px;top:162px">Lorem ipsum dolor sit amet, consectetuer adipiscing elit.</p>
  <div class="col-divider" style="left:107px"></div>

  <span class="num col-num" style="left:127px">02</span>
  <svg class="col-icon" style="left:161px" width="14" height="14" viewBox="0 0 14 14" fill="none" stroke="#fff" stroke-width=".8">
    <circle cx="7" cy="7" r="6"/><path d="M7 3.5V7l2.2 1.6"/>
  </svg>
  <p class="col-sub" style="left:114px">Subsection Title</p>
  <p class="para col-para" style="left:114px">Lorem ipsum dolor sit amet, consectetuer adipiscing elit. Aenean commodo ligula eget dolor. Aenean massa.</p>
  <p class="sub col-bullet" style="left:118px;top:147px">Lorem ipsum dolor sit amet, consectetuer adipiscing elit.</p>
  <p class="sub col-bullet" style="left:118px;top:162px">Lorem ipsum dolor sit amet, consectetuer adipiscing elit.</p>
  <div class="col-divider" style="left:196px"></div>

  <span class="num col-num" style="left:212px">03</span>
  <svg class="col-icon" style="left:247px" width="14" height="14" viewBox="0 0 14 14" fill="none" stroke="#fff" stroke-width=".8">
    <path d="M5 9 4 6.5C6 3 9 1 13 1c0 4-2 7-5.5 9z"/><circle cx="9.3" cy="4.7" r="1.2"/><path d="M4 6.5 1.5 7 3 4.5h3M7.5 10 7 12.5 9.5 11V8M4.5 9.5 1 13"/>
  </svg>
  <p class="col-sub" style="left:202px">Subsection Title</p>
  <p class="para col-para" style="left:202px">Lorem ipsum dolor sit amet, consectetuer adipiscing elit. Aenean commodo ligula eget dolor. Aenean massa.</p>
  <p class="sub col-bullet" style="left:206px;top:147px">Lorem ipsum dolor sit amet, consectetuer adipiscing elit.</p>
  <p class="sub col-bullet" style="left:206px;top:162px">Lorem ipsum dolor sit amet, consectetuer adipiscing elit.</p>
  <div class="col-divider" style="left:285px"></div>

  <span class="num col-num" style="left:294px">04</span>
  <svg class="col-icon" style="left:330px" width="17" height="15" viewBox="0 0 17 15" fill="none" stroke="#fff" stroke-width=".8">
    <path d="M5 3.5C5.8 2 7.8 1 10 1c3.3 0 6 2 6 4.6 0 1.4-.8 2.6-2 3.4l.6 2.2-2.4-1.3"/>
    <ellipse cx="6.5" cy="8" rx="5.5" ry="4.2"/><path d="M3 11.3 2 14l3-1.8"/><path d="M4 7.2h5M4 9h3.5"/>
  </svg>
  <p class="col-sub" style="left:290px">Subsection Title</p>
  <p class="para col-para" style="left:290px">Lorem ipsum dolor sit amet, consectetuer adipiscing elit. Aenean commodo ligula eget dolor. Aenean massa.</p>
  <p class="sub col-bullet" style="left:294px;top:147px">Lorem ipsum dolor sit amet, consectetuer adipiscing elit.</p>
  <p class="sub col-bullet" style="left:294px;top:162px">Lorem ipsum dolor sit amet, consectetuer adipiscing elit.</p>

  <div class="footer-rule"></div>
  <div class="footer-mark"><i></i>TALLOW</div>
  <p class="copyright">©Copyright 2023 Tallow Microsystems.</p>
  <p class="slide-num">SLIDE #</p>
</section>

<!-- 6 · Header with image -->
<section class="slide" style="left:443px;top:492px">
  <div class="topbar"></div>
  <div class="title-rule" style="left:40px;top:63px"></div>
  <h2 class="title" style="left:40px;top:73px;font-size:20px;line-height:1.2;letter-spacing:1.4px">CONTENT<br><span class="hl">HEADER</span><br>SLIDE</h2>
  <div role="img" aria-label="Photo: hand touching a glowing blue circuit-brain interface" style="left:197px;top:3px;width:189px;height:189px;background:radial-gradient(circle at 62% 52%,#7fd4ff 0%,#2a8ff0 35%,#0b4fc4 75%,#083a9a 100%)"></div>
  <p style="left:247px;top:84px;font-size:11px;font-weight:700;letter-spacing:1px;line-height:1.3">INSERT YOUR<br>IMAGE HERE</p>

  <div class="footer-rule"></div>
  <div class="footer-mark"><i></i>TALLOW</div>
  <p class="copyright">©Copyright 2023 Tallow Microsystems.</p>
  <p class="slide-num">SLIDE #</p>
</section>

<!-- 7 · Charts -->
<section class="slide" style="left:47px;top:719px">
  <div class="topbar reverse"></div>
  <div class="title-rule" style="left:51px;top:24px"></div>
  <h2 class="title" style="left:51px;top:30px">CONTENT <span class="hl">HEADER</span> SLIDE</h2>
  <p style="left:0;width:386px;top:69px;text-align:center;font-size:6.8px;color:var(--soft)">YOUR CONTENT GRAPHS STYLE</p>

  <svg style="left:0;top:0" width="386" height="217" viewBox="0 0 386 217" font-family="Montserrat,sans-serif" font-weight="600" fill="#fff">
    <g class="line-chart">
      <g stroke="var(--grid)" stroke-width=".5">
        <path d="M30 87h184M30 100h184M30 113h184M30 126h184M30 139h184M30 152h184M30 165h184M30 169h184"/>
        <path d="M30 87v82M45 87v82M62 87v82M79 87v82M96 87v82M113 87v82M130 87v82M147 87v82M164 87v82M181 87v82M198 87v82M214 87v82"/>
      </g>
      <polygon points="45,139 62,132.5 79,152 96,139 113,139 130,113 147,119.5 164,106.5 181,119.5 198,119.5 198,169 45,169" fill="#ffffff" fill-opacity=".08"/>
      <polyline points="45,139 62,132.5 79,152 96,139 113,139 130,113 147,119.5 164,106.5 181,119.5 198,119.5" fill="none" stroke="#fff" stroke-width=".8"/>
      <g fill="#fff">
        <circle cx="45" cy="139" r="1.6"/><circle cx="62" cy="132.5" r="1.6"/><circle cx="79" cy="152" r="1.6"/><circle cx="96" cy="139" r="1.6"/><circle cx="113" cy="139" r="1.6"/><circle cx="130" cy="113" r="1.6"/><circle cx="147" cy="119.5" r="1.6"/><circle cx="164" cy="106.5" r="1.6"/><circle cx="181" cy="119.5" r="1.6"/><circle cx="198" cy="119.5" r="1.6"/>
      </g>
      <g font-size="4.6" text-anchor="middle">
        <text x="23" y="89">70</text><text x="23" y="102">60</text><text x="23" y="115">50</text><text x="23" y="128">40</text><text x="23" y="141">30</text><text x="23" y="154">20</text><text x="23" y="167">10</text><text x="26" y="179">0</text>
        <text x="45" y="179">2015</text><text x="62" y="179">2016</text><text x="79" y="179">2017</text><text x="96" y="179">2018</text><text x="113" y="179">2019</text><text x="130" y="179">2020</text><text x="147" y="179">2021</text><text x="164" y="179">2022</text><text x="181" y="179">2023</text><text x="198" y="179">2024</text>
      </g>
    </g>
    <g class="bar-chart">
      <g fill="none" stroke="#6f7f88" stroke-width=".6">
        <rect x="233" y="87" width="14" height="82"/><rect x="256" y="87" width="14" height="82"/><rect x="278" y="87" width="14" height="82"/><rect x="301" y="87" width="14" height="82"/><rect x="324" y="87" width="14" height="82"/><rect x="346" y="87" width="14" height="82"/>
      </g>
      <g fill="var(--accent)">
        <rect x="233" y="159" width="14" height="10"/><rect x="256" y="151" width="14" height="18"/><rect x="278" y="143" width="14" height="26"/><rect x="301" y="133" width="14" height="36"/><rect x="324" y="123" width="14" height="46"/><rect x="346" y="114" width="14" height="55"/>
      </g>
      <g font-size="4.3" text-anchor="middle">
        <text x="240" y="166">15%</text><text x="263" y="162">25%</text><text x="285" y="158">35%</text><text x="308" y="153">55%</text><text x="331" y="147">65%</text><text x="353" y="143">75%</text>
      </g>
      <g font-size="4.6" text-anchor="middle">
        <text x="240" y="179">2019</text><text x="263" y="179">2020</text><text x="285" y="179">2021</text><text x="308" y="179">2022</text><text x="331" y="179">2023</text><text x="353" y="179">2024</text>
      </g>
    </g>
  </svg>

  <div class="footer-rule"></div>
  <div class="footer-mark"><i></i>TALLOW</div>
  <p class="copyright">©Copyright 2023 Tallow Microsystems.</p>
  <p class="slide-num">SLIDE #</p>
</section>

<!-- 8 · Title only -->
<section class="slide" style="left:443px;top:719px">
  <svg style="left:0;top:0" width="386" height="192" viewBox="0 0 386 192" fill="none">
    <defs>
      <linearGradient id="arcBlue" x1="0" y1="0" x2="1" y2="1">
        <stop offset="0" stop-color="var(--deep-blue)"/><stop offset="1" stop-color="var(--bright-blue)"/>
      </linearGradient>
    </defs>
    <circle cx="352" cy="-35" r="117" stroke="url(#arcBlue)" stroke-width="32"/>
    <circle cx="-50" cy="230" r="134" stroke="url(#arcBlue)" stroke-width="32"/>
  </svg>
  <div class="topbar reverse"></div>
  <h2 class="title" style="left:111px;top:77px;font-size:24px;line-height:1.2;letter-spacing:1.2px">YOUR <span class="hl">TITLE</span><br>SLIDE</h2>

  <div class="footer-rule"></div>
  <div class="footer-mark"><i></i>TALLOW</div>
  <p class="copyright">©Copyright 2023 Tallow Microsystems.</p>
  <p class="slide-num">SLIDE #</p>
</section>

<!-- 9 · Break -->
<section class="slide" style="left:47px;top:945px">
  <div class="topbar reverse"></div>
  <svg style="left:170px;top:61px" width="48" height="46" viewBox="0 0 48 46" fill="none" stroke="#fff" stroke-width="1.3" stroke-linecap="round">
    <path d="M12 2c-2 2 2 4 0 6s2 4 0 6M20 2c-2 2 2 4 0 6s2 4 0 6M28 2c-2 2 2 4 0 6s2 4 0 6"/>
    <path d="M6 24h28v10a8 8 0 0 1-8 8H14a8 8 0 0 1-8-8z"/>
    <path d="M34 27h4a4 4 0 0 1 0 8h-4"/>
    <path d="M2 44h36"/>
    <rect x="16" y="28" width="7" height="8"/><path d="M19.5 24v4"/>
  </svg>
  <h2 class="title" style="left:0;width:386px;text-align:center;top:119px;font-size:19px;letter-spacing:1.4px">BREAK <em class="hl" style="font-style:italic">SLIDE</em></h2>

  <div class="footer-rule"></div>
  <div class="footer-mark"><i></i>TALLOW</div>
  <p class="copyright">©Copyright 2023 Tallow Microsystems.</p>
  <p class="slide-num">SLIDE #</p>
</section>

<!-- 10 · Closing -->
<section class="slide" style="left:443px;top:945px">
  <svg style="left:0;top:0" width="386" height="192" viewBox="0 0 386 192" fill="none">
    <defs>
      <linearGradient id="arcBlueClose" x1="0" y1="0" x2="1" y2="1">
        <stop offset="0" stop-color="var(--deep-blue)"/><stop offset="1" stop-color="var(--bright-blue)"/>
      </linearGradient>
    </defs>
    <circle cx="360" cy="-50" r="118" stroke="url(#arcBlueClose)" stroke-width="32"/>
  </svg>
  <div class="topbar reverse"></div>
  <div style="left:46px;top:72px;width:26px;height:26px;border:3px solid var(--ink);border-radius:50%"></div>
  <p style="left:84px;top:64px;font-size:36px;font-weight:600;line-height:1;letter-spacing:1px">Tallow</p>
  <p style="left:86px;top:106px;font-size:17px;font-weight:600;line-height:1;letter-spacing:.6px">Microsystems</p>

  <div class="footer-rule"></div>
  <div class="footer-mark"><i></i>TALLOW</div>
  <p class="copyright">©Copyright 2023 Tallow Microsystems.</p>
  <p class="slide-num">SLIDE #</p>
</section>

</body>
</html>
```